Buch-/eBook-Cover für Autobiografie
Das Disign von dem Cover hat mir auf Anhieb sehr gut gefallen. Das hat gleich "ins schwarze" getroffen. Die Kommunikation war effizient und zielgerichtet
Zielgruppe
Ich bin eine Privatperson und habe im Laufe der letzten Jahre mein Autobiografie geschrieben. Besser gesagt ist es ein autobiografischer Roman geworden. Ich plane dieses Buch meiner Frau und meinen Söhnen und deren Familien zu schenken. Darüber hinaus ist es aber auch geplant das Buch bei Veltaro zu veröffentlichen.
Aufgabenstellung
Auf dem Cover sollte neben meinem Namen Konrad(a) Pelzmann natürlich auch der Titel von dem Buch stehen. Ich habe dem Buch den Titel gegeben: 'Das Licht am Ufer'. Auf dem Backcover hatte ich mir eine kurze zusammenfassung vorgestellt, die ich auch beifüge. Ich hatte geplant, das sowohl auf dem Cover, wie auch auf dem Backcover Bilder von mir (u.a. als Baby) mit gestaltet werden. Aber das ist nur so eine Idee, ich bin da für Vorschläge offen
Das Design darf nicht zu überladen sein.

```html
<!DOCTYPE html>
<html lang="de">
<head>
<meta charset="utf-8">
<title>Das Licht am Ufer – Cover und Rückseite</title>
<link rel="stylesheet" href="https://fonts.googleapis.com/css2?family=Libre+Caslon+Display&family=Libre+Caslon+Text:ital,wght@0,400;1,400&display=swap">
<style>
  :root {
    --backdrop: #efe9e4;
    --ink: #1f1a17;
    --ink-soft: #3a322d;
    --muted: #4a413b;
    --rule-rose: #b88a80;
    --rule-grey: #9a918b;
    --paper: #fbf5f1;
    --paper-lower: #f8efeb;
    --sepia-light: #e6d6cc;
    --sepia-mid: #c9b1a3;
    --sepia-dark: #8f7567;
  }
  * { margin: 0; padding: 0; box-sizing: border-box; }
  html, body {
    width: 1200px; height: 800px; overflow: hidden;
    background: var(--backdrop);
  }
  .stage { position: relative; width: 1200px; height: 800px; }

  .book {
    position: absolute; top: 87px; height: 636px;
    box-shadow: 2px 4px 10px rgba(60, 40, 30, 0.18);
    overflow: hidden;
  }

  /* Front cover */
  .front-cover { left: 119px; width: 442px; }
  .cover-photo {
    position: absolute; inset: 0;
    background:
      radial-gradient(ellipse 45% 40% at 42% 72%, var(--sepia-dark) 0%, rgba(143,117,103,0) 100%),
      linear-gradient(180deg, var(--sepia-light) 0%, #d9c4b8 45%, var(--sepia-mid) 100%);
  }
  .front-title {
    position: absolute; left: 86px; top: 58px;
    font-family: "Libre Caslon Display", "Times New Roman", serif;
    font-size: 56px; line-height: 64px; font-weight: 400;
    color: var(--ink); letter-spacing: -0.5px;
  }
  .front-rule {
    position: absolute; left: 86px; top: 198px; width: 268px; height: 1px;
    background: var(--rule-rose);
  }
  .front-author {
    position: absolute; left: 86px; top: 218px;
    font-family: "Libre Caslon Text", "Times New Roman", serif;
    font-size: 14px; letter-spacing: 3.4px; color: var(--ink-soft);
  }

  /* Back cover */
  .back-cover { left: 637px; width: 445px; background: var(--paper); }
  .back-lower {
    position: absolute; left: 0; right: 0; top: 425px; bottom: 0;
    background: var(--paper-lower);
  }
  .back-title {
    position: absolute; left: 63px; top: 52px;
    font-family: "Libre Caslon Display", "Times New Roman", serif;
    font-size: 68px; line-height: 72px; font-weight: 400;
    color: var(--ink); letter-spacing: -0.5px;
  }
  .back-rule {
    position: absolute; left: 63px; top: 214px; width: 230px; height: 1px;
    background: var(--rule-grey);
  }
  .blurb {
    position: absolute; left: 63px; top: 233px; width: 300px;
    font-family: "Libre Caslon Text", "Times New Roman", serif;
    font-size: 13.2px; line-height: 24px; color: var(--ink-soft);
  }
  .divider { position: absolute; left: 0; top: 413px; width: 445px; height: 26px; }
  .about-heading {
    position: absolute; left: 63px; top: 461px;
    font-family: "Libre Caslon Text", "Times New Roman", serif;
    font-size: 14px; color: var(--ink);
  }
  .about-text {
    position: absolute; left: 63px; top: 487px; width: 300px;
    font-family: "Libre Caslon Text", "Times New Roman", serif;
    font-style: italic; font-size: 11.6px; line-height: 21px; color: var(--muted);
  }
</style>
</head>
<body>
<main class="stage">
  <section class="book front-cover">
    <div class="cover-photo" role="img" aria-label="Sepiafoto: kleiner Junge mit Strohhut auf einem Dreirad im Garten vor einem Haus"></div>
    <h1 class="front-title">Das Licht<br>am Ufer</h1>
    <div class="front-rule"></div>
    <p class="front-author">KONRAD(A) PELZMANN</p>
  </section>

  <section class="book back-cover">
    <div class="back-lower"></div>
    <h2 class="back-title">Das Licht<br>am Ufer</h2>
    <div class="back-rule"></div>
    <p class="blurb">
      Eine autobiographische Erzählung<br>
      über Kindheit, Veränderung und<br>
      Identität, die von der Vergangenheit<br>
      bis in die Gegenwart reicht – und der Suche,<br>
      der eigenen Version sich zu finden,<br>
      dort, wo alles begann.
    </p>
    <svg class="divider" viewBox="0 0 445 26" aria-hidden="true">
      <line x1="0" y1="13" x2="61" y2="13" stroke="#d9bfb6" stroke-width="1"/>
      <line x1="100" y1="13" x2="445" y2="13" stroke="#d9bfb6" stroke-width="1"/>
      <circle cx="74" cy="13" r="11" fill="none" stroke="#2b2420" stroke-width="1.2"/>
      <path d="M74 6.5 V13 H78.5" fill="none" stroke="#2b2420" stroke-width="1.2"/>
    </svg>
    <h3 class="about-heading">Über die Autorin / den Autor</h3>
    <p class="about-text">
      Konrad(a) Pelzmann ist geboren und aufgewachsen<br>
      in Deutschland. Das Licht am Ufer ist sein/ihr<br>
      schriftstellerisches Debüt.
    </p>
  </section>
</main>
</body>
</html>
```